Ecommerce Website For Printing Company

Quillbarn.com are a print, design and signage company who sell flyers, business cards, posters, brochures and more to customers in the UK.

Our website is outdated and requires a new design using current web styling and mobile functionality.

We require the following pages to be designed;
- Home Page
- Price Page
- Portfolio Page
- Blog
- Content Page

Our competitors in the printing industry are www.tavenink.com, www.marlowpress.co.uk, brightquire.co.uk, www.leafcrate.co.uk

We require the website to give a professional image as well as be easy for customers to navigate, understand and find prices.

Target Market(s)

Businesses

Industry/Entity Type

Printing

Number of Pages Required

4 page

Font styles to use
Sans Serif

Colors
33a6d7

Requirements
Must have
• Popular products, latest news/blog, sales from portfolio, newsletter sign up, footer

```html
<!DOCTYPE html>
<html lang="en">
<head>
<meta charset="utf-8">
<title>Quillbarn.com – Sticker, Label &amp; Printing</title>
<link rel="stylesheet" href="https://fonts.googleapis.com/css2?family=Montserrat:wght@400;600;700&family=Open+Sans:wght@400;600&display=swap">
<style>
:root{
  --brand:#33a6d7;
  --brand-deep:#1f86bd;
  --brand-light:#8fd0ee;
  --ink:#2b2b2b;
  --muted:#8a8a8a;
  --paper:#ffffff;
  --soft:#f1f1f1;
  --dark:#1b1b1d;
  --black:#050505;
  --navy:#0f5a86;
}
*{box-sizing:border-box;margin:0;padding:0}
html,body{width:1200px;height:3272px;overflow:hidden}
body{font-family:"Open Sans",Arial,sans-serif;color:var(--ink);background:var(--paper)}
h1,h2,h3,h4,.nav a,.btn{font-family:"Montserrat",Arial,sans-serif}
.section-title{text-align:center;font-size:30px;font-weight:600;letter-spacing:1px;color:var(--ink)}

/* header */
.site-header{height:80px;display:flex;align-items:center;justify-content:space-between;padding:0 232px}
.brand{display:flex;align-items:center;gap:10px;font-family:"Montserrat",Arial,sans-serif;font-weight:700;font-size:26px;color:var(--brand)}
.brand-dot{width:14px;height:14px;border-radius:50%;background:var(--brand)}
.nav{display:flex;gap:14px}
.nav a{font-size:11px;font-weight:600;color:var(--muted);text-decoration:none;padding:8px 14px;letter-spacing:.5px}
.nav a.active{border:1px solid var(--brand);color:var(--brand)}

/* hero */
.hero{height:560px;background:linear-gradient(180deg,var(--brand) 0%,#4cb4e0 60%,#cfe9f6 100%);text-align:center;color:#fff;position:relative}
.hero-kicker{padding-top:76px;font-size:22px;font-weight:600;letter-spacing:1px}
.hero-title{font-size:40px;font-weight:700;margin-top:12px;letter-spacing:1px}
.btn{display:inline-block;background:var(--navy);color:#fff;font-size:12px;font-weight:600;padding:12px 26px;letter-spacing:1px;margin-top:36px}
.hero-visual{position:absolute;left:360px;top:250px;width:480px;height:270px;border-radius:6px;background:linear-gradient(135deg,#e9f6fc,#3b8fbf 60%,#0d4f78)}

/* portfolio */
.portfolio{height:648px;padding-top:40px}
.filters{display:flex;justify-content:center;gap:14px;margin-top:26px}
.filters span{font-size:11px;padding:5px 14px;border:1px solid #ccc;color:var(--muted)}
.filters span.on{background:var(--brand);border-color:var(--brand);color:#fff}
.portfolio-grid{display:grid;grid-template-columns:repeat(7,1fr);grid-template-rows:192px 192px;margin-top:26px}
.tile{display:block}
.more{text-align:center;font-size:12px;font-weight:600;margin-top:16px;font-family:"Montserrat",Arial,sans-serif}
.plus{width:42px;height:42px;border-radius:50%;background:var(--navy);margin:16px auto 0;display:flex;align-items:center;justify-content:center}

/* about */
.about{height:368px;background:var(--brand-light);position:relative}
.about-card{position:absolute;left:232px;top:56px;width:232px;height:256px;background:rgba(20,30,40,.88);color:#fff;padding:26px 22px}
.about-card h3{font-size:13px;font-weight:600;letter-spacing:1px}
.about-card p{font-size:10px;line-height:1.6;color:#cfd6db;margin-top:22px}
.about-card .btn{margin-top:22px;padding:8px 16px;font-size:10px}
.about-visual{position:absolute;left:500px;top:40px;width:480px;height:300px;background:linear-gradient(120deg,#244f6b,#3aa0cf 55%,#e6eef2)}

/* products */
.products{height:524px;padding-top:48px}
.product-grid{display:grid;grid-template-columns:repeat(3,236px);gap:10px 10px;justify-content:center;margin-top:36px}
.product{height:168px;position:relative}
.product .label{position:absolute;left:0;right:0;bottom:0;height:30px;background:var(--brand);color:#fff;font-size:10px;font-weight:600;display:flex;align-items:center;justify-content:center;letter-spacing:.5px;font-family:"Montserrat",Arial,sans-serif}

/* blog */
.blog{height:620px;background:var(--soft);padding-top:48px}
.blog-images{display:grid;grid-template-columns:repeat(3,1fr);height:156px;margin-top:38px}
.blog-posts{background:var(--dark);height:232px;display:grid;grid-template-columns:repeat(3,1fr);padding:30px 36px 0}
.post h4{color:var(--brand);font-size:13px;font-weight:600}
.post p{color:#b9b9b9;font-size:10px;line-height:1.7;margin-top:16px;padding-right:40px}
.post a{display:block;color:var(--brand);font-size:10px;margin-top:14px;text-decoration:none}
.blog .plus{margin-top:28px}

/* newsletter */
.newsletter{height:212px;text-align:center;padding-top:20px}
.newsletter .plus{margin:0 auto}
.newsletter h2{font-size:24px;font-weight:600;margin-top:14px;letter-spacing:1px}
.newsletter p{font-size:11px;color:var(--muted);margin-top:8px}
.signup{display:flex;justify-content:center;margin-top:20px}
.signup span{width:480px;height:32px;border:1px solid #ddd;text-align:left;font-size:11px;color:#aaa;padding:8px 12px}
.signup b{width:180px;height:32px;background:var(--navy);color:#fff;font-size:11px;font-weight:600;display:flex;align-items:center;justify-content:center;font-family:"Montserrat",Arial,sans-serif}

/* footer */
.site-footer{height:252px;background:var(--black);color:#ddd;padding-top:42px}
.contacts{display:grid;grid-template-columns:repeat(3,1fr);width:700px;margin:0 auto;text-align:center}
.contact .icon{width:44px;height:44px;border-radius:50%;background:var(--brand);margin:0 auto;display:flex;align-items:center;justify-content:center}
.contact p{font-size:11px;margin-top:10px;line-height:1.5}
.social{display:flex;justify-content:center;gap:12px;margin-top:24px}
.social span{width:22px;height:22px;border-radius:50%;background:#3a3a3a}
.copyright{text-align:center;font-size:10px;color:#888;margin-top:12px}
</style>
</head>
<body>

<header class="site-header">
  <div class="brand"><span class="brand-dot"></span>Quillbarn.com</div>
  <nav class="nav">
    <a class="active">HOME</a><a>ABOUT</a><a>PORTFOLIO</a><a>BLOG</a><a>NEWS</a><a>CONTACT</a>
  </nav>
</header>

<section class="hero">
  <h2 class="hero-kicker">WE BRING THE BEST QUALITY</h2>
  <h1 class="hero-title">STICKER, LABEL &amp; PRINTING</h1>
  <span class="btn">GET YOURS NOW</span>
  <div class="hero-visual" role="img" aria-label="Fanned stack of printed brochures and leaflets"></div>
</section>

<section class="portfolio">
  <h2 class="section-title">OUR PORTFOLIO</h2>
  <div class="filters"><span class="on">All</span><span>Flyers</span><span>Leaflet Design</span><span>Gallery Design</span></div>
  <div class="portfolio-grid">
    <div class="tile" role="img" aria-label="Purple brochure sample" style="background:linear-gradient(135deg,#5b3b8c,#d8d0e8)"></div>
    <div class="tile" role="img" aria-label="Blue company brochure" style="background:linear-gradient(135deg,#1c4f80,#6fb1d8)"></div>
    <div class="tile" role="img" aria-label="White and blue leaflet" style="background:linear-gradient(135deg,#e8eef3,#2f7fb5)"></div>
    <div class="tile" role="img" aria-label="Green landscape brochure" style="background:linear-gradient(135deg,#3b8a4a,#cfe6c5)"></div>
    <div class="tile" role="img" aria-label="Blue tri-fold flyer" style="background:linear-gradient(135deg,#0e5c92,#e2eef5)"></div>
    <div class="tile" role="img" aria-label="Corporate flyer set" style="background:linear-gradient(135deg,#21466d,#9fc4df)"></div>
    <div class="tile" role="img" aria-label="Red and blue flyer set" style="background:linear-gradient(135deg,#c9362f,#2b6aa6)"></div>
    <div class="tile" role="img" aria-label="Report cover pages" style="background:linear-gradient(135deg,#f2f4f6,#9ab8cc)"></div>
    <div class="tile" role="img" aria-label="Hexagon pattern brochure" style="background:linear-gradient(135deg,#2a9fd4,#f0f6fa)"></div>
    <div class="tile" role="img" aria-label="Teal business flyer" style="background:linear-gradient(135deg,#1a8aa0,#e3f1f3)"></div>
    <div class="tile" role="img" aria-label="Dark blue brochure spread" style="background:linear-gradient(135deg,#0b2f52,#4f8fc0)"></div>
    <div class="tile" role="img" aria-label="Colourful square pattern flyer" style="background:linear-gradient(135deg,#e84a5f,#f5c344 50%,#2ab1a3)"></div>
    <div class="tile" role="img" aria-label="Blue event flyer" style="background:linear-gradient(135deg,#2463a8,#a7cbe9)"></div>
    <div class="tile" role="img" aria-label="Red promotional flyers" style="background:linear-gradient(135deg,#d8322a,#f4d7d3)"></div>
  </div>
  <p class="more">WANT TO SEE MORE?</p>
  <div class="plus"><svg width="16" height="16"><path d="M8 2v12M2 8h12" stroke="#fff" stroke-width="2.5"/></svg></div>
</section>

<section class="about">
  <div class="about-card">
    <h3>ABOUT QUILLBARN</h3>
    <p>We print flyers, cards, posters and brochures for busy businesses across the UK. Fast turnaround, sharp colour and friendly help from proof to delivery. Order online in minutes and track every job.</p>
    <span class="btn">Read More</span>
  </div>
  <div class="about-visual" role="img" aria-label="Open brochures and printed catalogue pages"></div>
</section>

<section class="products">
  <h2 class="section-title">OUR PRODUCTS</h2>
  <div class="product-grid">
    <div class="product" role="img" aria-label="Flyer printing sample" style="background:linear-gradient(135deg,#e9ecef,#7d8a95)"><span class="label">FLYER PRINTING</span></div>
    <div class="product" role="img" aria-label="Brochure printing sample" style="background:linear-gradient(135deg,#1d5c93,#dbe8f2)"><span class="label">BROCHURE PRINTING</span></div>
    <div class="product" role="img" aria-label="Business card printing sample" style="background:linear-gradient(135deg,#f3f3f3,#2fb1b7)"><span class="label">BUSINESS CARDS</span></div>
    <div class="product" role="img" aria-label="Leaflet printing sample" style="background:linear-gradient(135deg,#3b9fd0,#e8f4fa)"><span class="label">LEAFLET PRINTING</span></div>
    <div class="product" role="img" aria-label="Poster printing sample" style="background:linear-gradient(135deg,#2f6f3a,#d7e9d2)"><span class="label">POSTER PRINTING</span></div>
    <div class="product" role="img" aria-label="Sticker and label sample" style="background:linear-gradient(135deg,#dfe6ec,#3a7fb8)"><span class="label">STICKERS</span></div>
  </div>
</section>

<section class="blog">
  <h2 class="section-title">OUR BLOG</h2>
  <div class="blog-images">
    <div role="img" aria-label="Photo of customers reviewing prints" style="background:linear-gradient(135deg,#c98a4b,#6b4a2e)"></div>
    <div role="img" aria-label="Colour swatch fan for print matching" style="background:linear-gradient(135deg,#e9b93a,#c23a5a 50%,#3a6fc2)"></div>
    <div role="img" aria-label="Large format printer in use" style="background:linear-gradient(135deg,#f1f1f1,#4d6d9a 60%,#e23b2e)"></div>
  </div>
  <div class="blog-posts">
    <article class="post"><h4>THE BLOG TITLE</h4><p>Simple ways to make your next flyer stand out. Choose bold colour, clear type and a single message your customers remember long after they read it.</p><a>Read More</a></article>
    <article class="post"><h4>THE BLOG TITLE</h4><p>Colour matching explained for print buyers. Learn how swatches, proofs and paper stock work together to keep your brand looking the same on every job.</p><a>Read More</a></article>
    <article class="post"><h4>THE BLOG TITLE</h4><p>Large format printing for shops and events. Banners, posters and signs that grab attention, printed quickly on durable media and shipped to your door.</p><a>Read More</a></article>
  </div>
  <div class="plus"><svg width="16" height="16"><path d="M8 2v12M2 8h12" stroke="#fff" stroke-width="2.5"/></svg></div>
</section>

<section class="newsletter">
  <div class="plus"><svg width="18" height="14"><rect x="1" y="1" width="16" height="12" fill="none" stroke="#fff" stroke-width="1.6"/><path d="M1 1l8 7 8-7" fill="none" stroke="#fff" stroke-width="1.6"/></svg></div>
  <h2>NEWSLETTER</h2>
  <p>Keep updated with our latest news by subscribing our newsletter</p>
  <div class="signup"><span>E-mail</span><b>SUBSCRIBE</b></div>
</section>

<footer class="site-footer">
  <div class="contacts">
    <div class="contact">
      <div class="icon"><svg width="18" height="18"><path d="M4 2h3l1.5 4-2 1.3a9 9 0 0 0 4.2 4.2L12 9.5l4 1.5v3a2 2 0 0 1-2 2A12 12 0 0 1 2 4a2 2 0 0 1 2-2z" fill="#fff"/></svg></div>
      <p>0117 496 0832</p>
    </div>
    <div class="contact">
      <div class="icon"><svg width="18" height="14"><rect x="1" y="1" width="16" height="12" fill="none" stroke="#fff" stroke-width="1.6"/><path d="M1 1l8 7 8-7" fill="none" stroke="#fff" stroke-width="1.6"/></svg></div>
      <p>hello@quillbarn.com</p>
    </div>
    <div class="contact">
      <div class="icon"><svg width="14" height="20"><path d="M7 1a6 6 0 0 1 6 6c0 5-6 12-6 12S1 12 1 7a6 6 0 0 1 6-6z" fill="#fff"/><circle cx="7" cy="7" r="2.2" fill="#33a6d7"/></svg></div>
      <p>48 Harbour Lane<br>Bristol BS1 4QA</p>
    </div>
  </div>
  <div class="social"><span></span><span></span><span></span><span></span></div>
  <p class="copyright">© 2024 Quillbarn.com. All Rights Reserved.</p>
</footer>

</body>
</html>
```